Rate Card

We wish to update our rate card flyer.I have uploaded a copy of our current version, which has a black background but we want to redesign this with a cleaner and fresh look with a white background. Our new logo also needs to be used.

The stats on the why choose us need to be updated also.

- 8,000+ sales agreed
- £2.1bn sales value
- £41m savings
- 97.5% recommended
- 5,000 client testimonials

We would like a new look to this double sided flyer.

This is an urgent requirement so anyone that posts a design we like quickly will more than likely get this order!

```html
<!DOCTYPE html>
<html lang="en">
<head>
<meta charset="utf-8">
<title>Home Circle – Rate Card</title>
<link rel="stylesheet" href="https://fonts.googleapis.com/css2?family=Montserrat:wght@600;700;800&family=Open+Sans:wght@400;600;700&display=swap">
<style>
:root{
  --backdrop:#000;
  --paper:#fff;
  --ink:#333;
  --ink-soft:#444;
  --grey-cell:#e4e5e7;
  --pink:#e93d8f;
  --blue:#27bdec;
  --green:#8cc63f;
  --purple:#6b2c91;
  --red:#b0161e;
  --sky-blue:#2a9bd6;
  --orange:#f28b1e;
}
*{margin:0;padding:0;box-sizing:border-box}
html,body{width:852px;height:1200px;overflow:hidden;background:var(--backdrop)}
.canvas{position:relative;width:852px;height:1200px;background:var(--backdrop)}
.side{position:absolute;left:23px;width:809px;height:569px;background:var(--paper);color:var(--ink);font-family:"Open Sans",sans-serif}
.side--front{top:19px}
.side--back{top:607px}

.title{position:absolute;font-family:"Montserrat",sans-serif;font-weight:800;color:var(--ink);letter-spacing:-1px;line-height:1}
.fee-title{left:0;right:0;top:58px;text-align:center;font-size:58px}

.fee-table{position:absolute;left:68px;top:155px;display:grid;grid-template-columns:188px 160px 160px 160px;grid-auto-rows:63px;gap:2px;font-family:"Montserrat",sans-serif}
.fee-table div{display:flex;align-items:center;justify-content:center;text-align:center}
.cell-head{background:var(--grey-cell);font-weight:600;font-size:21px;color:var(--ink)}
.cell-label{background:var(--grey-cell);font-weight:700;font-size:21px;color:var(--ink)}
.cell{color:#fff;font-weight:700;font-size:22px}
.cell--pink{background:var(--pink)}
.cell--blue{background:var(--blue)}
.cell--green{background:var(--green)}
.cell--small{font-size:15px;line-height:1.25;padding:0 10px}

.footnote{position:absolute;right:68px;top:422px;font-size:8px;color:var(--ink-soft)}
.advertised{position:absolute;left:68px;top:443px;font-family:"Montserrat",sans-serif;font-weight:700;font-size:15px}
.portal{position:absolute;top:494px;font-family:"Open Sans",sans-serif;font-weight:700;font-size:19px;display:flex;align-items:center;gap:6px}
.portal i{display:inline-block;width:14px;height:14px;background:var(--green)}
.portal--one{left:68px;color:#222}
.portal--two{left:225px;color:#4b1f5e}
.portal--three{left:368px;color:#1e5fa8}
.brand{position:absolute;display:flex;align-items:center;gap:10px;font-family:"Montserrat",sans-serif;font-weight:700;color:var(--ink)}
.brand i{display:inline-block;background:var(--pink)}
.brand--front{left:552px;top:470px;font-size:26px}
.brand--front i{width:40px;height:40px}

.why-title{left:46px;top:48px;font-size:58px}
.featured-label{position:absolute;left:608px;top:40px;font-family:"Montserrat",sans-serif;font-weight:700;font-size:16px}
.badge{position:absolute;border-radius:2px}
.badge--one{left:608px;top:71px;width:64px;height:28px;background:var(--sky-blue)}
.badge--two{left:676px;top:71px;width:65px;height:28px;background:var(--red)}
.badge--three{left:606px;top:104px;width:135px;height:32px;background:linear-gradient(#f4f4f4,#cfcfcf)}

.col-heading{position:absolute;font-family:"Montserrat",sans-serif;font-weight:600;font-size:20px;line-height:26px;color:var(--ink)}
.col-heading--stats{left:48px;top:124px}
.col-heading--service{left:404px;top:146px}
.ticks{position:absolute;list-style:none;font-weight:700;font-size:14.5px;color:var(--ink-soft)}
.ticks li{position:relative;padding-left:12px;line-height:19px;margin-bottom:8px}
.ticks li::before{content:"";position:absolute;left:0;top:6px;border-left:5px solid #555;border-top:4px solid transparent;border-bottom:4px solid transparent}
.ticks--stats{left:48px;top:184px;width:320px}
.ticks--service{left:404px;top:178px;width:340px}

.review-badge{position:absolute;left:96px;top:437px;width:190px;height:56px;border-radius:8px;background:var(--purple)}
.stars{position:absolute;left:138px;top:500px;display:flex;gap:2px}

.address{position:absolute;left:526px;top:386px;display:flex;gap:20px}
.address i{display:block;width:44px;height:44px;background:var(--pink);margin-top:4px}
.address p{font-size:12px;line-height:16px;color:var(--ink)}
.address .address-name{font-weight:600;font-size:14px;line-height:20px}
.phone{display:inline-flex;align-items:center;gap:4px}
</style>
</head>
<body>
<div class="canvas">

  <section class="side side--front">
    <h1 class="title fee-title">fee menu</h1>

    <div class="fee-table">
      <div class="cell-head"></div>
      <div class="cell-head">upfront</div>
      <div class="cell-head">completion</div>
      <div class="cell-head">total</div>

      <div class="cell-label">no commision</div>
      <div class="cell cell--pink">£495+VAT</div>
      <div class="cell cell--pink">£0</div>
      <div class="cell cell--pink">£495+VAT</div>

      <div class="cell-label">commision</div>
      <div class="cell cell--blue">£195+VAT</div>
      <div class="cell cell--blue">£795+VAT</div>
      <div class="cell cell--blue">£990+VAT</div>

      <div class="cell-label">no sale-no fee</div>
      <div class="cell cell--green">£0</div>
      <div class="cell cell--green cell--small">we'll beat any quote*</div>
      <div class="cell cell--green cell--small">we'll beat any quote*</div>
    </div>

    <p class="footnote">* subject to a minimum fee of £1000+VAT</p>
    <p class="advertised">Your property advertised on:</p>
    <span class="portal portal--one"><i></i>Nestfinder</span>
    <span class="portal portal--two">Dwellio</span>
    <span class="portal portal--three">KeyPlace</span>
    <div class="brand brand--front"><i></i>Home Circle</div>
  </section>

  <section class="side side--back">
    <h2 class="title why-title">why choose us ?</h2>

    <p class="featured-label">As Featured on</p>
    <span class="badge badge--one"></span>
    <span class="badge badge--two"></span>
    <span class="badge badge--three"></span>

    <h3 class="col-heading col-heading--stats">Strenght in numbers<br>since our launch in 2003</h3>
    <ul class="ticks ticks--stats">
      <li>8,000+ sales agreed</li>
      <li>£2.1bn sales value</li>
      <li>£41m savings vs high street fees</li>
      <li>£4,500 average fee SAVING vs high street</li>
      <li>97.5% recommended by our clients</li>
      <li>5,000 client testimonials</li>
      <li>9/10 average client rating</li>
      <li>Rated no.2 estate agent in the UK by the independent Verdict Hub</li>
    </ul>

    <span class="review-badge"></span>
    <svg class="stars" width="104" height="20" viewBox="0 0 104 20" aria-hidden="true">
      <g fill="var(--orange)">
        <polygon points="10,1 12.6,7 19,7.4 14,11.6 15.6,18 10,14.4 4.4,18 6,11.6 1,7.4 7.4,7"/>
        <polygon transform="translate(21 0)" points="10,1 12.6,7 19,7.4 14,11.6 15.6,18 10,14.4 4.4,18 6,11.6 1,7.4 7.4,7"/>
        <polygon transform="translate(42 0)" points="10,1 12.6,7 19,7.4 14,11.6 15.6,18 10,14.4 4.4,18 6,11.6 1,7.4 7.4,7"/>
        <polygon transform="translate(63 0)" points="10,1 12.6,7 19,7.4 14,11.6 15.6,18 10,14.4 4.4,18 6,11.6 1,7.4 7.4,7"/>
        <polygon transform="translate(84 0)" points="10,1 12.6,7 19,7.4 14,11.6 15.6,18 10,14.4 4.4,18 6,11.6 1,7.4 7.4,7"/>
      </g>
    </svg>

    <h3 class="col-heading col-heading--service">Customer service</h3>
    <ul class="ticks ticks--service">
      <li>Personal account manager with direct dial</li>
      <li>Online account to track your progress</li>
      <li>All staff are NPEA qualified</li>
      <li>Weekly activity reports keep you in the loop</li>
      <li>Live web chat facility after hours</li>
      <li>Full personal estate agency service from instruction to completion</li>
    </ul>

    <div class="address">
      <i></i>
      <p>
        <span class="address-name">Home Circle</span><br>
        Estate Offices<br>
        Ashby Meadow Farm<br>
        Ashby Meadow Road<br>
        Ashby Meadow<br>
        Essex&nbsp; CM9 2QX<br>
        <span class="phone"><svg width="10" height="10" viewBox="0 0 10 10" aria-hidden="true"><path d="M2 0.5 L3.6 2.6 L2.7 3.6 Q4 6 6.4 7.3 L7.4 6.4 L9.5 8 L8.3 9.5 Q3.5 8.8 0.5 1.7 Z" fill="#333"/></svg>0845 000 1234</span><br>
        www.homecircle.co.uk
      </p>
    </div>
  </section>

</div>
</body>
</html>
```